Business Card Design Project

I need a business card designed for FableHarbor, a website which has people share their fictional story ideas with others. The business cards should incorporate the websites's logo, which can be found at www.fableharbor-example.com .

Target Market(s)

These will be primarily used in business development activities, not given to customers. It therefore needs to have a clean, professional appearance, and yet communicate what the company is trying to achieve as a bold startup.

Industry/Entity Type

Business

```html
<!DOCTYPE html>
<html lang="en">
<head>
<meta charset="UTF-8">
<title>FableHarbor Business Card</title>
<link rel="stylesheet" href="https://fonts.googleapis.com/css2?family=Arimo:wght@400;700&display=swap">
<style>
  :root {
    --page: #ffffff;
    --navy: #23456a;
    --mist: #cfdfef;
    --mist-light: #e4edf7;
    --white: #ffffff;
  }
  * { margin: 0; padding: 0; box-sizing: border-box; }
  html, body {
    width: 1200px;
    height: 1000px;
    overflow: hidden;
    background: var(--page);
  }
  .canvas {
    position: relative;
    width: 1200px;
    height: 1000px;
  }
  .card {
    position: absolute;
    left: 308px;
    height: 307px;
    overflow: hidden;
  }
  .card-front {
    top: 132px;
    width: 553px;
    background: var(--navy);
  }
  .brand {
    position: absolute;
    left: 89px;
    top: 128px;
    display: flex;
    align-items: center;
    gap: 18px;
  }
  .brand-dot {
    width: 54px;
    height: 54px;
    border-radius: 50%;
    background: var(--mist);
  }
  .brand-name {
    font-family: "Arimo", Arial, sans-serif;
    font-weight: 400;
    font-size: 42px;
    letter-spacing: 0.5px;
    color: var(--white);
    line-height: 1;
  }
  .card-back {
    top: 532px;
    width: 550px;
    height: 305px;
    background: var(--mist);
  }
  .motif {
    position: absolute;
    right: 0;
    top: 0;
    width: 360px;
    height: 305px;
    background: radial-gradient(ellipse at 60% 45%, var(--mist-light) 0%, rgba(228,237,247,0.5) 45%, rgba(207,223,239,0) 75%);
  }
  .contact {
    position: absolute;
    left: 64px;
    top: 60px;
    font-family: "Arimo", Arial, sans-serif;
    font-weight: 700;
    color: var(--navy);
  }
  .contact-name { font-size: 32px; line-height: 38px; }
  .contact-title { font-size: 24px; line-height: 30px; margin-top: 4px; }
  .contact-lines { list-style: none; margin-top: 6px; }
  .contact-lines li { font-size: 24px; line-height: 32px; }
</style>
</head>
<body>
<main class="canvas">
  <section class="card card-front" aria-label="Card front">
    <div class="brand">
      <span class="brand-dot" aria-hidden="true"></span>
      <span class="brand-name">FableHarbor</span>
    </div>
  </section>

  <section class="card card-back" aria-label="Card back">
    <div class="motif" role="img" aria-label="Faint oversized brand motif decoration"></div>
    <div class="contact">
      <p class="contact-name">Name</p>
      <p class="contact-title">Title</p>
      <ul class="contact-lines">
        <li>E: xxxxxx@xxxxx</li>
        <li>P: xx xxxx xxxx</li>
        <li>M: xx xxxx xxxx</li>
      </ul>
    </div>
  </section>
</main>
</body>
</html>
```